Informational Site for Advanced Chemistry R&D

The company develops oxidation chemistry for air, water, fuel pollution controls. The site has been prototyped at www.velkorlabs.net. Take a look. Now, the task is to design it for eye-catching beauty with use of color, on-page scroll-driven color transition and parallax effects. Should capture the themes: high technology, wow it's beautiful, modern, uncluttered, clean urban environment.

Target Market(s)

China Environmentally Conscious Government and Industry,

Industry/Entity Type

It Company

Number of Pages Required

3 page

Font styles to use
Sans Serif

Requirements
Must have
• Parallax effects, desktop compatible, Rich, Modern, Simple, Graphic
Nice to have
• Mobile Phone Compatible
Should not have
• Flash, or anything that is slow to load or requires high bandwidth

```html
<!DOCTYPE html>
<html lang="en">
<head>
<meta charset="utf-8">
<title>VelkorLabs — Advanced Oxidation Science</title>
<link rel="stylesheet" href="https://fonts.googleapis.com/css2?family=Barlow:wght@400;500;600;700&display=swap">
<style>
:root{
  --teal:#2bb7b5;
  --teal-dark:#219e9c;
  --blue:#0c5eb0;
  --blue-deep:#063a86;
  --navy:#03123d;
  --ink:#333a40;
  --muted:#7b838a;
  --white:#ffffff;
  --footer:#efefef;
  --map:#dcdcdc;
}
*{margin:0;padding:0;box-sizing:border-box}
html,body{width:1200px;height:3136px;overflow:hidden}
body{font-family:"Barlow",Arial,sans-serif;color:var(--ink);background:var(--white);position:relative}
section,header,footer{position:absolute;left:0;width:1200px}
.abs{position:absolute}

/* header */
.site-header{top:0;height:109px;background:var(--white)}
.brand{left:178px;top:30px;display:flex;align-items:center;gap:10px;font-size:25px;font-weight:600;color:var(--teal)}
.brand-dot{width:16px;height:16px;border-radius:50%;background:var(--teal)}
.nav{top:46px;font-size:15px;letter-spacing:.5px;color:#3a4148}
.nav.active{color:var(--blue)}
.nav-underline{left:655px;top:86px;width:62px;height:3px;background:var(--blue)}

/* hero */
.hero{top:109px;height:456px;background:radial-gradient(ellipse at 30% 20%,#1b5fd6 0%,#0a2b8e 35%,var(--navy) 75%);color:var(--white)}
.hero-brand{left:0;width:1200px;top:150px;text-align:center;font-size:28px;font-weight:600;display:flex;justify-content:center;align-items:center;gap:10px}
.hero-brand .brand-dot{background:var(--white)}
.hero-title{left:0;width:1200px;top:228px;text-align:center;font-size:32px;line-height:40px;font-weight:400}
.slide-arrow{top:210px;width:34px;height:34px;border-radius:50%;background:var(--teal)}

/* technology */
.technology{top:565px;height:654px;background:var(--teal);color:var(--white)}
.section-title{left:0;width:1200px;text-align:center;font-size:28px;font-weight:700;letter-spacing:1px}
.tech-sub{left:0;width:1200px;top:132px;text-align:center;font-size:22px;line-height:31px}
.tech-item{width:290px;text-align:center}
.tech-icon{margin:0 auto;width:130px;height:130px;border-radius:50%;background:var(--blue);display:flex;align-items:center;justify-content:center}
.tech-label{margin-top:42px;font-size:24px;letter-spacing:1px}
.tech-text{margin-top:16px;font-size:11px;line-height:20px}

/* advanced oxidation */
.oxidation{top:1219px;height:495px;background:linear-gradient(90deg,#0b69b9,var(--blue) 60%,#0a55a6)}
.ox-photo{left:134px;top:81px;width:462px;height:330px;border:6px solid #d9e2ea;background:linear-gradient(135deg,#9fc7e4,#3f86c4 50%,#1a4f8f);box-shadow:0 6px 16px rgba(0,0,0,.35)}
.ox-copy{left:612px;top:100px;width:440px;color:var(--white)}
.ox-copy h2{font-size:28px;font-weight:700;letter-spacing:.5px;margin-bottom:12px}
.ox-copy p{font-size:14px;line-height:24px}
.ox-copy ul{list-style:none;margin:22px 0 40px}
.ox-copy li{font-size:14px;line-height:34px;padding-left:26px;position:relative}
.ox-copy li::before{content:"›";position:absolute;left:2px;top:-1px;font-size:18px}

/* solutions */
.solutions{top:1714px;height:631px;background:var(--white)}
.solutions .section-title{top:50px;color:var(--teal)}
.card{top:117px;width:287px;height:401px;box-shadow:0 8px 14px rgba(0,0,0,.22)}
.card-photo{height:196px}
.card-body{height:205px;background:var(--teal);color:var(--white);text-align:center;padding:24px 26px 0}
.card-body h3{font-size:14px;font-weight:600;margin-bottom:18px}
.card-body p{font-size:11px;line-height:19px}
.pager{top:560px;width:28px;height:28px;border-radius:50%;background:#9a9a9a}

/* contact */
.contact{top:2345px;height:414px;background:var(--map)}
.map{left:447px;top:0;width:753px;height:414px;background:linear-gradient(135deg,#e4e4e4,#cfcfcf)}
.contact-panel{left:0;top:0;width:447px;height:414px;background:linear-gradient(135deg,#1a68c2,var(--blue-deep));color:var(--white);padding:72px 0 0 154px}
.contact-panel h2{font-size:24px;font-weight:600;margin-bottom:24px}
.contact-row{display:flex;gap:18px;font-size:14px;line-height:20px;margin-bottom:16px}
.contact-row svg{flex:none;margin-top:2px}
.contact-note{font-size:12px;line-height:19px;width:280px;margin-top:4px}
.contact-cta{font-size:13px;font-weight:700;margin-top:12px}

/* partners */
.partners{top:2759px;height:251px;background:var(--white)}
.partners .section-title{top:38px;font-size:18px;color:var(--teal)}
.partner{top:94px;width:220px;text-align:center}
.partner-name{height:100px;display:flex;align-items:center;justify-content:center;gap:8px;font-size:24px;font-weight:600;color:var(--teal)}
.partner-name.red{color:#d0212b}
.partner-badge{margin:0 auto;width:94px;height:94px;border-radius:50%}
.partner-caption{margin-top:10px;font-size:12px;color:var(--muted)}

/* footer */
.site-footer{top:3010px;height:126px;background:var(--footer);font-size:11px;color:#555;letter-spacing:.3px}
</style>
</head>
<body>

<header class="site-header">
  <div class="abs brand"><span class="brand-dot"></span>VelkorLabs</div>
  <a class="abs nav active" style="left:662px">HOME</a>
  <a class="abs nav" style="left:756px">TECHNOLOGY</a>
  <a class="abs nav" style="left:899px">PRODUCTS</a>
  <a class="abs nav" style="left:1024px">CONTACT</a>
  <div class="abs nav-underline"></div>
</header>

<section class="hero" role="img" aria-label="Dark blue backdrop of glowing molecular hexagons">
  <div class="abs hero-brand"><span class="brand-dot"></span>VelkorLabs</div>
  <h1 class="abs hero-title">Advanced Oxidation<br>Science for Environmental Pollution<br>Management</h1>
  <div class="abs slide-arrow" style="left:60px"><svg width="34" height="34"><path d="M19 11l-6 6 6 6" stroke="#fff" stroke-width="2.5" fill="none"/></svg></div>
  <div class="abs slide-arrow" style="left:1105px"><svg width="34" height="34"><path d="M15 11l6 6-6 6" stroke="#fff" stroke-width="2.5" fill="none"/></svg></div>
</section>

<section class="technology">
  <h2 class="abs section-title" style="top:68px">TECHNOLOGY</h2>
  <p class="abs tech-sub">Environmental pollution control solutions employing nature’s most<br>reactive Free Radical</p>

  <div class="abs tech-item" style="left:141px;top:263px">
    <div class="tech-icon"><svg width="44" height="54" viewBox="0 0 44 54"><path d="M22 2C14 16 4 26 4 35a18 18 0 0 0 36 0C40 26 30 16 22 2z" fill="#fff"/></svg></div>
    <div class="tech-label">WATER</div>
    <p class="tech-text">Lorem ipsum dolor sit amet, consectetur adipiscing elit, sed do eiusmod tempor incididunt ut labore et dolore magna aliqua. Ut enim ad minim veniam, quis nostrud exercitation ullamco laboris nisi ut aliquip ex ea commodo consequat.</p>
  </div>
  <div class="abs tech-item" style="left:453px;top:263px">
    <div class="tech-icon"><svg width="64" height="44" viewBox="0 0 64 44"><path d="M14 40a12 12 0 0 1-2-24 16 16 0 0 1 30-6 12 12 0 0 1 12 14 9 9 0 0 1-2 16z" fill="#fff"/><text x="24" y="32" font-family="Barlow,sans-serif" font-size="14" font-weight="700" fill="#0c5eb0">O²</text></svg></div>
    <div class="tech-label">AIR</div>
    <p class="tech-text">Lorem ipsum dolor sit amet, consectetur adipiscing elit, sed do eiusmod tempor incididunt ut labore et dolore magna aliqua. Ut enim ad minim veniam, quis nostrud exercitation ullamco laboris nisi ut aliquip ex ea commodo consequat.</p>
  </div>
  <div class="abs tech-item" style="left:752px;top:263px">
    <div class="tech-icon"><svg width="50" height="58" viewBox="0 0 50 58"><rect x="4" y="4" width="28" height="50" rx="3" fill="#fff"/><rect x="9" y="10" width="18" height="12" fill="#0c5eb0"/><path d="M32 16l8 6v22a3 3 0 0 0 6 0V14l-6-6" stroke="#fff" stroke-width="3" fill="none"/></svg></div>
    <div class="tech-label">FUEL</div>
    <p class="tech-text">Lorem ipsum dolor sit amet, consectetur adipiscing elit, sed do eiusmod tempor incididunt ut labore et dolore magna aliqua. Ut enim ad minim veniam, quis nostrud exercitation ullamco laboris nisi ut aliquip ex ea commodo consequat.</p>
  </div>
</section>

<section class="oxidation">
  <div class="abs ox-photo" role="img" aria-label="Laboratory scene with a microscope, a green leaf and a glowing data wave"></div>
  <div class="abs ox-copy">
    <h2>ADVANCED OXIDATION</h2>
    <p>Advanced Oxidation refers to a &nbsp;variety of techniques employing the Hydroxyl Radical, an energetic, highly reactive cousin of the water molecule:</p>
    <ul>
      <li>To add oxygen to inorganic molecules</li>
      <li>To remove hydrogen from organic molecules</li>
    </ul>
    <p>These transformations convert important industrial contaminants into reactive forms that can be captured or that disintegrate into harmless end products.</p>
  </div>
</section>

<section class="solutions">
  <h2 class="abs section-title">SOLUTIONS</h2>
  <article class="abs card" style="left:144px">
    <div class="card-photo" role="img" aria-label="Factory chimneys releasing smoke into a golden sky" style="background:linear-gradient(180deg,#d8b544,#8a6a2a 60%,#3c2e1a)"></div>
    <div class="card-body"><h3>Fuel Oil Desulfurization</h3><p>Our proprietary low temperature and pressure advanced oxidation catalytic process reliably removes sulfur from diesel transportation fuel at less than half the operating costs of older hydro-desulfurization processes.</p></div>
  </article>
  <article class="abs card" style="left:456px">
    <div class="card-photo" role="img" aria-label="Worker in a hard hat and respirator amid dark smoke" style="background:linear-gradient(180deg,#5a5e62,#9c9fa2 55%,#3a3d40)"></div>
    <div class="card-body"><h3>Volatile Organic Compunds (VOC)</h3><p>Alkanes, alkenes, halogenated hydrocarbons, aromatic hydrocarbons, esters, aldehydes, polycyclic aromatic hydrocarbons. We convert these by-products of industrial processes before they enter the atmosphere and cause smog.</p></div>
  </article>
  <article class="abs card" style="left:767px">
    <div class="card-photo" role="img" aria-label="Power plant cooling towers under a blue sky" style="background:linear-gradient(180deg,#4f86c4,#8fb6dc 55%,#6d7d8e)"></div>
    <div class="card-body"><h3>Flue Gas Scrubbing</h3><p>Our proprietary low temperature and pressure advanced oxidation catalytic process reliably removes sulfur from diesel transportation fuel at less than half the operating costs of older hydro-desulfurization processes.</p></div>
  </article>
  <div class="abs pager" style="left:569px"><svg width="28" height="28"><path d="M16 8l-6 6 6 6" stroke="#fff" stroke-width="2.5" fill="none"/></svg></div>
  <div class="abs pager" style="left:603px"><svg width="28" height="28"><path d="M12 8l6 6-6 6" stroke="#fff" stroke-width="2.5" fill="none"/></svg></div>
</section>

<section class="contact">
  <div class="abs map" role="img" aria-label="Street map showing the office location"></div>
  <div class="abs contact-panel">
    <h2>CONTACT US</h2>
    <div class="contact-row"><svg width="18" height="16" viewBox="0 0 18 16"><path d="M9 1L1 5h16z M2 6h14v1H2z M3 8h2v5H3z M8 8h2v5H8z M13 8h2v5h-2z M1 14h16v2H1z" fill="#fff"/></svg><span>Velkor Labs<br>CorporationMillbrook,<br>Delaware, U.S.A.</span></div>
    <div class="contact-row"><svg width="18" height="14" viewBox="0 0 18 14"><rect x="1" y="1" width="16" height="12" fill="none" stroke="#fff" stroke-width="1.6"/><path d="M1 1l8 7 8-7" fill="none" stroke="#fff" stroke-width="1.6"/></svg><span>info@velkorlabs.net</span></div>
    <div class="contact-row"><svg width="18" height="16" viewBox="0 0 18 18"><path d="M4 1l3 4-2 2c1 3 3 5 6 6l2-2 4 3-2 3C8 17 1 10 1 3z" fill="#fff"/></svg><span>+1 555 014 2288</span></div>
    <p class="contact-note">We welcome inquiries regarding the licensing, distribution, and purchase of our products, systems, and technologies.</p>
    <p class="contact-cta">Please contact us for more information.</p>
  </div>
</section>

<section class="partners">
  <h2 class="abs section-title">PARTNERS</h2>
  <div class="abs partner" style="left:120px">
    <div class="partner-name"><span class="brand-dot"></span>Corvane Systems</div>
    <p class="partner-caption">Our sales partner in China</p>
  </div>
  <div class="abs partner" style="left:371px">
    <div class="partner-name red">Tessaro</div>
    <p class="partner-caption">Our construction partner in China</p>
  </div>
  <div class="abs partner" style="left:607px">
    <div style="height:100px;padding-top:3px"><div class="partner-badge" style="border:3px solid #1b4f9a"></div></div>
    <p class="partner-caption">Our technology partner in China</p>
  </div>
  <div class="abs partner" style="left:824px">
    <div style="height:100px;padding-top:3px"><div class="partner-badge" style="border:3px solid #b3202a"></div></div>
    <p class="partner-caption">Our technology partner in China</p>
  </div>
</section>

<footer class="site-footer">
  <div class="abs" style="left:144px;top:40px">HOME &nbsp;&nbsp;|&nbsp;&nbsp; TECHNOLOGY &nbsp;&nbsp;|&nbsp;&nbsp; PRODUCTS &nbsp;&nbsp;|&nbsp;&nbsp; CONTACT</div>
  <div class="abs" style="left:144px;top:72px">© 2016 COMPANY NAME &nbsp;|&nbsp; ALL RIGHTS RESERVED</div>
  <div class="abs" style="left:990px;top:40px;display:flex;gap:10px">
    <span style="width:9px;height:9px;background:var(--teal);display:block"></span>
    <span style="width:9px;height:9px;background:var(--teal);display:block"></span>
    <span style="width:9px;height:9px;background:var(--teal);display:block"></span>
  </div>
  <div class="abs" style="left:857px;top:72px">TERMS OF SERVICE &nbsp;|&nbsp; PRIVACY POLICY</div>
</footer>

</body>
</html>
```